Natural deodorant label

Natural clean deodorant line. Need modernize label which can be sized for both the regular and travel size deodorants. 2.75 x 3" and 1x2". Important to highlight no baking soda and its natural. Also has no aluminum, preservatives, nor chemicals. Its gender inclusive and safe for all ages. Please see website at www.lorvatique.com. will attach current label. Will need a label that i would be able to update with new scents as they come. Want a clean look.
Updates

Need extra days to review

Target Market(s)

the working mother/wife that lives a clean healthy life and pushes that for her family

Industry/Entity Type

health and beauty/deodorant/natural

Colors

Designer to choose colors to be used in the design.

Requirements
Must have
• No baking soda and gender inclusive on label. Clean look. Very little to no picture art.
Nice to have
• Potentially a different color representing the different scents. A brief description of the deodorant scent underneath the scent name. This can be found under the drop down menu titled valdora deodorant scents on the website www.lorvatique.com. Area on front label for a small barcode.
Should not have
• misspelled words; dark label

```html
<!DOCTYPE html>
<html lang="en">
<head>
<meta charset="utf-8">
<title>Lorvatique – Valdora Deodorant Labels</title>
<link href="https://fonts.googleapis.com/css2?family=Cinzel:wght@400;600&family=Jost:wght@400;500&family=Montserrat:wght@500&display=swap" rel="stylesheet">
<style>
  :root {
    --page: #e9e9e9;
    --label: #ffffff;
    --ink: #111111;
    --orange: #f7a21b;
    --orange-deep: #f39200;
  }
  * { box-sizing: border-box; margin: 0; padding: 0; }
  html, body { width: 1200px; height: 720px; overflow: hidden; }
  body {
    background: var(--page);
    display: flex;
    align-items: center;
    justify-content: center;
    gap: 60px;
    color: var(--ink);
  }
  .label {
    width: 500px;
    height: 560px;
    background: var(--label);
    border-top: 9px solid var(--orange);
    border-bottom: 16px solid var(--orange);
    box-shadow: 0 6px 18px rgba(0,0,0,.18);
    display: flex;
    flex-direction: column;
    align-items: center;
    padding-top: 34px;
  }
  .brand {
    display: flex;
    flex-direction: column;
    align-items: center;
    gap: 8px;
  }
  .brand-dot {
    width: 58px; height: 58px;
    border-radius: 50%;
    background: var(--ink);
  }
  .brand-name {
    font-family: "Cinzel", serif;
    font-weight: 600;
    font-size: 34px;
    letter-spacing: 1px;
    line-height: 1;
  }
  .tagline {
    font-family: "Montserrat", sans-serif;
    font-size: 10px;
    letter-spacing: 3px;
    margin-top: 4px;
  }
  .scent-art {
    width: 330px;
    height: 120px;
    margin-top: 26px;
    border-radius: 60px;
    background: radial-gradient(ellipse at 55% 50%, var(--orange-deep) 0%, var(--orange) 45%, rgba(247,162,27,0.15) 75%, rgba(255,255,255,0) 100%);
  }
  .claims {
    margin-top: 26px;
    display: flex;
    gap: 8px;
    padding: 8px 12px;
    border: 2px solid var(--orange);
    border-radius: 40px;
  }
  .claim {
    width: 56px; height: 56px;
    border-radius: 50%;
    border: 2px solid var(--orange);
    display: flex;
    align-items: center;
    justify-content: center;
    text-align: center;
    font-family: "Jost", sans-serif;
    font-size: 7.5px;
    font-weight: 500;
    line-height: 1.1;
    padding: 4px;
  }
  .scent-name {
    font-family: "Cinzel", serif;
    font-size: 18px;
    letter-spacing: 3px;
    margin-top: 28px;
  }
  .scent-note {
    font-family: "Montserrat", sans-serif;
    font-size: 10px;
    letter-spacing: 3px;
    margin-top: 12px;
  }
  .net-weight {
    font-family: "Jost", sans-serif;
    font-size: 10px;
    margin-top: 6px;
  }
  .label--back .scent-art { margin-top: 20px; }
  .product-type {
    font-family: "Cinzel", serif;
    font-size: 22px;
    margin-top: 22px;
    letter-spacing: 1px;
  }
  .ingredients {
    position: relative;
    width: 430px;
    margin-top: 30px;
    border: 2px solid var(--orange);
    border-radius: 36px;
    padding: 24px 22px 16px;
    text-align: center;
    font-family: "Jost", sans-serif;
    font-size: 12.5px;
    line-height: 1.4;
  }
  .ingredients-title {
    position: absolute;
    top: -13px; left: 50%;
    transform: translateX(-50%);
    background: var(--orange);
    color: var(--ink);
    font-family: "Jost", sans-serif;
    font-weight: 500;
    font-size: 13px;
    padding: 3px 16px;
    border-radius: 14px;
    box-shadow: 0 0 0 8px var(--label);
  }
  .ethics {
    font-family: "Cinzel", serif;
    font-size: 14px;
    letter-spacing: 4px;
    text-align: center;
    line-height: 1.15;
    margin-top: 34px;
  }
  .recycle { margin-top: 8px; }
  .website {
    font-family: "Cinzel", serif;
    font-size: 15px;
    letter-spacing: 7px;
    margin-top: 10px;
  }
</style>
</head>
<body>

  <section class="label label--front">
    <div class="brand">
      <span class="brand-dot"></span>
      <span class="brand-name">Lorvatique</span>
      <span class="tagline">100% ORGANIC</span>
    </div>
    <div class="scent-art" role="img" aria-label="Hand-lettered Valdora script over an orange ink splash"></div>
    <div class="claims">
      <div class="claim">NO BAKING SODA</div>
      <div class="claim">NO ALUMINUM</div>
      <div class="claim">NO PRESERV&shy;ATIVES</div>
      <div class="claim">NO CHEMICALS</div>
    </div>
    <p class="scent-name">SOLSTICE</p>
    <p class="scent-note">NATURALLY REFRESHING</p>
    <p class="net-weight">NET WT 2.5oz (70g)</p>
  </section>

  <section class="label label--back">
    <div class="brand">
      <span class="brand-dot"></span>
      <span class="brand-name">Lorvatique</span>
    </div>
    <div class="scent-art" role="img" aria-label="Hand-lettered Valdora script over an orange ink splash"></div>
    <p class="product-type">UNISEX DEODORANT</p>
    <div class="ingredients">
      <span class="ingredients-title">INGREDIENTS</span>
      Raw alkaline coconut oil, Mango butter, arrowroot powder, candelilla wax, zinc ricinoleate, zinc powder, vitamin E oil, fragrance
    </div>
    <p class="ethics">CRUELTY FREE<br>VEGAN</p>
    <svg class="recycle" width="22" height="22" viewBox="0 0 24 24" aria-label="Recyclable">
      <g fill="none" stroke="#111" stroke-width="2.6" stroke-linejoin="round">
        <path d="M10 4 L4 15"/>
        <path d="M14 4 L19 12"/>
        <path d="M17 19 L7 19"/>
      </g>
      <g fill="#111">
        <path d="M16 9 l5 1 l-1 5z"/>
        <path d="M8 22 l-4 -3 l4 -3z"/>
        <path d="M8 3 l5 -1 l-1 5z"/>
      </g>
    </svg>
    <p class="website">WWW.LORVATIQUE.COM</p>
  </section>

</body>
</html>
```